Create a dynamic design for a photographers site

We need a design for a wordpress web site for a photography business specializing in Hotels, Resorts and Travel Destinations. We have a lot of experience in the US and Caribbean and offer the full service to the client from planning, to production and delivery of the final product.
We are looking for a clean, sharp, modern design with big visuals, options for video. We already have a logo which is blue and black.
Updates

With your designs, I'd like to see a second page as well as a front page. I would like it to have a content area and a side bar. Thanks You

Glen

Target Market(s)

Hotels and Marketing people. I'm selling commercial photography mainly to the travel industry with hotels, resorts and destination experiences. I also shoot for retail stores, restaurants. Also do lifestyle with models that fits into any of the above.

Industry/Entity Type

Business

Colors

Designer to choose colors to be used in the design.

Requirements
Must have
• Big visuals.
Opportunity to showcase video,
Social Media links,
Blog

```html
<!DOCTYPE html>
<html lang="en">
<head>
<meta charset="utf-8">
<title>Lakeside Lens Photography</title>
<link href="https://fonts.googleapis.com/css2?family=Roboto+Condensed:wght@300;400;700&display=swap" rel="stylesheet">
<style>
:root{
  --blue:#0a86c8;
  --blue-dark:#0773ad;
  --red:#d42a1f;
  --ink:#222;
  --text:#777;
  --rule:#444;
  --grey-bg:#f2f1f1;
  --white:#fff;
  --btn:#1b1b1b;
}
*{margin:0;padding:0;box-sizing:border-box}
html,body{width:865px;height:1200px;overflow:hidden;background:var(--white)}
body{position:relative;font-family:"Roboto Condensed",sans-serif;color:var(--ink)}
.abs{position:absolute}
.brand{left:36px;top:38px;font-size:27px;font-weight:400;color:var(--blue);letter-spacing:.5px}
.call{left:515px;top:24px;font-size:18px;font-weight:300;color:var(--red);white-space:nowrap}
.social{top:19px;width:28px;height:28px;border-radius:50%;background:var(--blue);border:2px solid #dce9f1}
.nav{left:357px;top:59px;font-size:15px;font-weight:300}
.nav a{color:var(--ink);text-decoration:none;position:absolute;top:0;white-space:nowrap}
.nav a.active{color:var(--blue);border-bottom:1px solid var(--blue);padding-bottom:2px}
.dropdown{left:572px;top:81px;width:103px;height:104px;background:var(--blue);padding:4px 9px;z-index:5}
.dropdown div{font-size:12px;color:var(--white);font-weight:400;height:20.5px;line-height:19px;border-bottom:1px dashed rgba(255,255,255,.8)}
.dropdown div:last-child{border:none}
.band{left:0;top:130px;width:865px;height:233px;background:var(--blue)}
.stage{left:36px;top:108px;width:793px;height:260px;background:var(--white)}
.slider{left:39px;top:112px;width:479px;height:250px;background:linear-gradient(180deg,#3a4a72 0%,#c46a3a 22%,#1b2230 45%,#27313d 80%,#4d5868 100%)}
.dots{left:250px;top:342px;display:flex;gap:8px}
.dots span{width:12px;height:12px;border-radius:50%;background:var(--white)}
.dots span:first-child{background:var(--blue)}
.arrow{top:215px;color:rgba(255,255,255,.6);font-size:48px;font-weight:300}
.video{left:523px;top:108px;width:304px;height:255px;background:#111}
.video-title{left:523px;top:108px;width:304px;height:22px;background:#111;color:#fff;font-size:13px;padding:4px 9px}
.more-video{left:757px;top:110px;width:70px;height:20px;background:#f0f0f0;color:var(--red);font-size:11px;text-align:center;line-height:20px}
.video-frame{left:525px;top:132px;width:300px;height:212px;background:linear-gradient(180deg,#b9a98a,#8a6b54 55%,#7a2a24 80%,#5b2520)}
.play{left:643px;top:208px;width:60px;height:60px;border-radius:50%;background:rgba(0,0,0,.45)}
.controls{left:525px;top:344px;width:300px;height:18px;background:#1c1c1c}
.time{left:728px;top:348px;font-size:7px;color:#ddd}
.shade{left:40px;top:362px;width:788px;height:10px;background:linear-gradient(#bbb,rgba(255,255,255,0));border-radius:50%;opacity:.6}
h2{font-weight:300;color:var(--blue);font-size:26px}
.col{width:240px}
.col p{font-size:12px;font-weight:300;color:var(--text);line-height:18px;text-align:justify}
.btn{background:var(--btn);color:var(--white);font-size:13px;height:22px;line-height:22px;padding:0 10px;border-radius:3px}
.post{left:586px;width:240px;height:36px;border-bottom:1px dashed var(--rule);font-size:11.5px;font-weight:300;color:var(--text);line-height:13px}
.post .who{color:var(--blue)}
.post .more{position:absolute;left:182px;top:13px;color:var(--red)}
.post .dot{position:absolute;left:92px;top:-4px;width:10px;height:10px;border-radius:50%;background:var(--blue)}
.grey{left:0;top:643px;width:865px;height:522px;background:var(--grey-bg)}
.section-title{width:865px;text-align:center;font-size:32px;font-weight:300;color:#333}
.pic{width:157px;height:106px}
.pic.city{background:linear-gradient(180deg,#1c3a66,#3f4b5e 45%,#b0563a 80%,#6a3a2a)}
.pic.island{background:linear-gradient(180deg,#1e5f9a,#3c8c8c 40%,#8a9a6a 60%,#2c87b0)}
.pager{width:157px;height:106px;background:#f7f7f7;border:1px solid #ddd;color:var(--blue);font-size:25px;font-weight:300;display:flex;align-items:center;justify-content:center;gap:6px}
.card{top:1015px;width:186px;height:124px;background:var(--white);border:1px solid #ddd;padding:4px;box-shadow:0 6px 8px -6px #999}
.card .ph{width:176px;height:114px;position:relative}
.card .lbl{position:absolute;left:0;right:0;bottom:8px;text-align:center;color:#fff;font-size:13px;font-weight:700;white-space:nowrap}
.footer{top:1177px;width:865px;text-align:center;font-size:9px;color:#555}
</style>
</head>
<body>
<header>
  <div class="abs brand">Lakeside Lens</div>
  <div class="abs call">CALL US : 555-010-2468</div>
  <div class="abs social" style="left:702px"></div>
  <div class="abs social" style="left:747px"></div>
  <div class="abs social" style="left:793px"></div>
  <nav class="abs nav">
    <a class="active" style="left:0">HOME</a>
    <a style="left:57px">ABOUT US</a>
    <a style="left:139px">SERVICES</a>
    <a style="left:217px">PORTFOLIO</a>
    <a style="left:303px">VIDEO</a>
    <a style="left:357px">BLOG</a>
    <a style="left:408px">REACH US</a>
  </nav>
  <div class="abs dropdown"><div>HOTELS</div><div>DESTINATIONS</div><div>RETAIL</div><div>LIFESTYLE</div><div>FASHION</div></div>
</header>

<section class="hero">
  <div class="abs band"></div>
  <div class="abs stage"></div>
  <div class="abs slider" role="img" aria-label="Aerial night view of a resort hotel and city skyline at dusk"></div>
  <div class="abs arrow" style="left:46px">‹</div>
  <div class="abs arrow" style="left:488px">›</div>
  <div class="abs dots"><span></span><span></span><span></span><span></span></div>
  <div class="abs video"></div>
  <div class="abs video-title">TODAY V</div>
  <div class="abs more-video">MORE VIDEO</div>
  <div class="abs video-frame" role="img" aria-label="Video still of a hotel atrium lobby with red seating"></div>
  <div class="abs play"><svg width="60" height="60"><polygon points="24,19 24,41 41,30" fill="#fff"/></svg></div>
  <div class="abs controls"><svg width="300" height="18"><polygon points="6,5 6,13 12,9" fill="#fff"/><rect x="18" y="7" width="180" height="4" fill="#555"/><rect x="18" y="7" width="70" height="4" fill="#1a9ae0"/><rect x="85" y="5" width="6" height="8" fill="#ddd"/><rect x="268" y="8" width="20" height="2" fill="#777"/><rect x="288" y="4" width="8" height="9" fill="none" stroke="#ddd"/></svg></div>
  <div class="abs time">4:25 / 7:12</div>
  <div class="abs shade"></div>
</section>

<section class="intro">
  <h2 class="abs" style="left:42px;top:411px">ABOUT US</h2>
  <div class="abs col" style="left:42px;top:450px"><p>Since 2003, Lakeside Lens Photography has been capturing beauty around the globe while making sure to catch the natural beauty found right at home in lakeside, Florida. An artistic eye with a professional corporate know-how, Lakeside Lens Photography specializes in travel, corporate, and hotel photography.</p></div>
  <div class="abs btn" style="left:207px;top:592px">READ MORE</div>

  <h2 class="abs" style="left:310px;top:411px">SERVICES</h2>
  <div class="abs col" style="left:310px;top:450px"><p>On location photo shoots,post-production images, privately hosted galleries, and a top-notch professional eye for detail. See what Lakeside Lens Photography has to offer.</p></div>
  <div class="abs btn" style="left:475px;top:592px">READ MORE</div>

  <h2 class="abs" style="left:586px;top:411px">LATEST POSTS</h2>
  <div class="abs post" style="top:451px">Hotels &amp; Travel<span class="dot"></span><br>Tweets from a list by <span class="who">Glen Marlow</span><span class="more">MORE &gt;&gt;</span></div>
  <div class="abs post" style="top:499px">Hotels &amp; Travel<span class="dot"></span><br>Tweets from a list by <span class="who">Glen Marlow</span><span class="more">MORE &gt;&gt;</span></div>
  <div class="abs post" style="top:547px">Hotels &amp; Travel<span class="dot"></span><br>Tweets from a list by <span class="who">Glen Marlow</span><span class="more">MORE &gt;&gt;</span></div>
  <div class="abs btn" style="left:750px;top:592px">READ MORE</div>
</section>

<section class="gallery">
  <div class="abs grey"></div>
  <div class="abs section-title" style="left:0;top:662px">LATEST PICS</div>
  <div class="abs pic city" style="left:36px;top:715px" role="img" aria-label="Downtown street with theater sign at night"></div>
  <div class="abs pic island" style="left:194px;top:715px" role="img" aria-label="Aerial view of a tropical island coastline"></div>
  <div class="abs pic city" style="left:352px;top:715px" role="img" aria-label="Downtown street with theater sign at night"></div>
  <div class="abs pic island" style="left:510px;top:715px" role="img" aria-label="Aerial view of a tropical island coastline"></div>
  <div class="abs pic city" style="left:669px;top:715px" role="img" aria-label="Downtown street with theater sign at night"></div>
  <div class="abs pic island" style="left:36px;top:823px" role="img" aria-label="Aerial view of a tropical island coastline"></div>
  <div class="abs pic city" style="left:194px;top:823px" role="img" aria-label="Downtown street with theater sign at night"></div>
  <div class="abs pic island" style="left:352px;top:823px" role="img" aria-label="Aerial view of a tropical island coastline"></div>
  <div class="abs pager" style="left:511px;top:823px"><svg width="12" height="24"><polygon points="11,0 11,24 1,12" fill="var(--blue)"/></svg>PREVIOUS</div>
  <div class="abs pager" style="left:670px;top:823px">NEXT<svg width="12" height="24"><polygon points="1,0 1,24 11,12" fill="var(--blue)"/></svg></div>

  <div class="abs section-title" style="left:0;top:962px">WE OFFER</div>
  <div class="abs card" style="left:37px"><div class="ph" role="img" aria-label="Beach lounging scene by turquoise water" style="background:linear-gradient(180deg,#8cc6e6,#2fb2c8 45%,#e8d8b8)"><span class="lbl">ON LOCATION PHOTO SHOOTS</span></div></div>
  <div class="abs card" style="left:239px"><div class="ph" role="img" aria-label="Aerial view of a historic tower and town" style="background:linear-gradient(180deg,#9fb8d4,#b79a78 50%,#5c6a4a)"><span class="lbl">AERIAL PHOTOGRAPHY</span></div></div>
  <div class="abs card" style="left:441px"><div class="ph" role="img" aria-label="Aerial view of a resort bay and marina" style="background:linear-gradient(180deg,#8aa0b0,#3f7f9a 45%,#6a8a6a)"><span class="lbl">THE FULL PACKAGE</span></div></div>
  <div class="abs card" style="left:639px"><div class="ph" role="img" aria-label="Team reviewing photos on a laptop" style="background:linear-gradient(180deg,#c8c86a,#3a4a3a 50%,#1f2a3a)"><span class="lbl">PHOTO SHOOT STEP-BY-STEP</span></div></div>
</section>

<footer class="abs footer" style="left:0">Privacy | Terms | 2014 lakesidelensphoto.com</footer>
</body>
</html>
```